文章や画像はこちらでWARDにて提供します。こちら提供のもの使わずイラストや写真をそちらで新たに加える事も可能です。こちらの画像で高画質画像が必要な場合は提供します。
チラシ全体の配置とデザインをお願いします。
現時点でまだ会場などが未定でデザインが出来上がってからの加筆修正が必要です。
一般社団法人森川暮らし連盟
A4
片面
緑系
• 高解像度JPG (.jpg)
• イラストレーター形式 (.ai)
画像を添付します。

オリジナリティーと趣旨を理解し応用したイラストと洗練されたデザインが決め手となりました。

選定したランサーの案が出てくるまでは選ぶの非常に困難な程沢山の良い案を作成して頂き有難う御座います。今後チラシの趣旨次第では他のランサーの方に御依頼をする可能性があります。今後とも宜しくお願い致します。

```html
<!DOCTYPE html>
<html lang="ja">
<head>
<meta charset="UTF-8">
<title>口栄士資格制度セミナー</title>
<link href="https://fonts.googleapis.com/css2?family=M+PLUS+Rounded+1c:wght@500;700;800&family=Noto+Sans+JP:wght@400;500;700;900&display=swap" rel="stylesheet">
<style>
:root{
  --green:#3fa535;
  --green-dark:#23872b;
  --green-pale:#e6f3d6;
  --cream:#f6f8ea;
  --yellow:#fff45c;
  --ink:#333;
  --white:#fff;
}
*{margin:0;padding:0;box-sizing:border-box}
html,body{width:849px;height:1200px;overflow:hidden;background:var(--white)}
.flyer{position:relative;width:849px;height:1200px;overflow:hidden;
  font-family:"Noto Sans JP",sans-serif;color:var(--ink);
  background:linear-gradient(180deg,#f3f8e8 0%,#f3f8e8 60%,var(--cream) 100%)}
.art-veg{position:absolute;left:0;top:410px;width:849px;height:110px;
  background:linear-gradient(90deg,#f2d79a55,#e9a07a44 30%,#b9d98a55 60%,#e6c27a55);
  border-radius:0 0 40px 40px}
.format-tag{position:absolute;left:268px;top:10px;width:312px;height:34px;
  background:var(--green);color:var(--white);font-weight:700;font-size:20px;
  display:flex;align-items:center;justify-content:center;letter-spacing:1px}
.title-block{position:absolute;left:268px;top:44px;width:312px;height:350px;
  background:var(--yellow);display:flex;flex-direction:column;align-items:center;justify-content:center;
  font-family:"M PLUS Rounded 1c",sans-serif;font-weight:800;color:var(--green);line-height:1.1}
.title-block span{display:block;white-space:nowrap}
.title-block .t1{font-size:90px;letter-spacing:4px}
.title-block .t2,.title-block .t3{font-size:70px}
.point{position:absolute;background:var(--green);color:var(--white);
  font-weight:700;font-size:17px;line-height:1.4;padding:8px 12px;
  display:flex;align-items:center;justify-content:center;text-align:center}
.p-l1{left:23px;top:56px;width:234px;height:100px}
.p-l2{left:23px;top:185px;width:234px;height:95px}
.p-l3{left:23px;top:300px;width:234px;height:115px}
.p-r1{left:590px;top:34px;width:236px;height:178px;font-size:15px}
.p-r2{left:590px;top:228px;width:236px;height:110px}
.p-r3{left:590px;top:352px;width:236px;height:98px}
.photo{position:absolute;
  background:radial-gradient(circle at 50% 40%,#f3e0cf,#c9b39f 70%,#a78f7c)}
.photo-lead{left:28px;top:480px;width:255px;height:260px;border-radius:48% 48% 40% 40%}
.photo-guest{left:578px;top:468px;width:255px;height:260px;border-radius:48% 48% 40% 40%}
.course{position:absolute;left:318px;top:550px;width:232px;height:150px;
  background:var(--green);color:var(--white);
  font-family:"M PLUS Rounded 1c",sans-serif;font-weight:800;
  display:flex;flex-direction:column;align-items:center;justify-content:center;line-height:1.2}
.course .c1{font-size:44px;letter-spacing:2px}
.course .c2{font-size:44px;letter-spacing:8px}
.speaker{position:absolute;writing-mode:vertical-rl;background:var(--white);
  border:2px solid var(--green);color:var(--green-dark);font-weight:700;padding:8px 4px;font-size:22px;letter-spacing:2px}
.speaker small{font-size:14px;letter-spacing:1px}
.speaker-lead{left:262px;top:505px}
.speaker-guest{left:556px;top:495px}
.role{position:absolute;left:28px;top:832px;width:255px;text-align:center;font-size:16px;font-weight:500}
.guest-profile{position:absolute;left:596px;top:800px;width:240px;font-size:11px;line-height:1.6}
.date{position:absolute;left:300px;top:742px;width:290px;
  font-family:"M PLUS Rounded 1c",sans-serif;font-weight:800;color:var(--ink);font-size:50px;letter-spacing:1px;white-space:nowrap}
.date .day{color:var(--green-dark);font-size:64px}
.date .dow{font-size:28px;color:var(--green-dark)}
.venue{position:absolute;left:300px;top:830px;width:290px;font-size:26px;font-weight:700;white-space:nowrap}
.schedule{position:absolute;left:85px;top:905px;width:680px;border-collapse:collapse;font-size:17px;font-weight:700}
.schedule td{height:35px;padding:0 10px;border-bottom:1px dashed #9cc58a;white-space:nowrap}
.schedule .time{width:190px;color:var(--green-dark);letter-spacing:1px}
.schedule .note{font-size:13px;font-weight:500}
.footer{position:absolute;left:0;top:1122px;width:849px;height:78px;background:var(--green);color:var(--white)}
.org{position:absolute;left:14px;top:8px;width:150px;height:62px;background:var(--white);color:var(--green);
  font-weight:700;font-size:12px;display:flex;align-items:center;gap:6px;padding:0 8px;border-radius:6px}
.org .dot{width:26px;height:26px;border-radius:50%;background:var(--green);flex:none}
.apply{position:absolute;left:185px;top:8px;font-size:23px;font-weight:900;color:var(--yellow)}
.url{position:absolute;left:185px;top:46px;font-size:16px;font-weight:500;letter-spacing:.5px}
.search{position:absolute;left:585px;top:12px;display:flex;align-items:center}
.search .box{width:150px;height:34px;background:var(--white);color:var(--ink);font-size:15px;font-weight:700;
  display:flex;align-items:center;padding-left:8px;border:2px solid var(--green-dark)}
.search .btn{height:34px;padding:0 10px;background:var(--green-dark);display:flex;align-items:center;gap:4px;font-size:15px;font-weight:700;border:2px solid var(--white)}
</style>
</head>
<body>
<div class="flyer">
  <div class="art-veg" role="img" aria-label="野菜や果物のイラストが並ぶ帯"></div>
  <div class="format-tag">リアル会場開催＋オンライン</div>
  <h1 class="title-block"><span class="t1">口栄士</span><span class="t2">資格制度</span><span class="t3">セミナー</span></h1>

  <p class="point p-l1">矯正治療、歯周病<br>治療の栄養学</p>
  <p class="point p-l2">歯科医院の健康<br>ステーション化</p>
  <p class="point p-l3">予防管理型歯科<br>医院のメンテナンス<br>定着率UP</p>
  <p class="point p-r1">口腔機能発達不全症、<br>上気道抵抗症候群、<br>口呼吸などを有する子供・<br>大人の背景には必ず<br>栄養の問題が</p>
  <p class="point p-r2">口腔機能発達不全<br>の治療の栄養学的<br>アプローチ</p>
  <p class="point p-r3">矯正治療、歯周病<br>治療の栄養学</p>

  <div class="photo photo-lead" role="img" aria-label="講師の人物写真"></div>
  <div class="photo photo-guest" role="img" aria-label="ゲスト講師の人物写真"></div>
  <p class="speaker speaker-lead"><small>講師</small> 森川 達也</p>
  <p class="speaker speaker-guest"><small>ゲスト講師</small> 高槻 美緒</p>

  <div class="course"><span class="c1">口腔機能</span><span class="c2">栄養学</span></div>

  <p class="date">2022/12/<span class="day">4</span><span class="dow">(日)</span></p>
  <p class="venue">会場：○○○○○○○○</p>

  <p class="role">森川暮らし連盟理事長</p>
  <p class="guest-profile">・タカツキ歯科クリニック マネージャー<br>・株式会社ミドリ ヘルスケア事業部<br>・管理栄養士 食育指導士<br>・オーガニックライフ講座 主宰</p>

  <table class="schedule">
    <tr><td class="time">11:00～12:00</td><td>口腔機能栄養学講演</td></tr>
    <tr><td class="time">12:00～13:00</td><td>休憩</td></tr>
    <tr><td class="time">13:00～14:00</td><td>ゲスト講師高槻美緒先生講演</td></tr>
    <tr><td class="time">14:15～15:45</td><td>口腔機能栄養学講演</td></tr>
    <tr><td class="time">15:45～16:00</td><td>テスト、採点、合格発表<span class="note">（再試可、免許証授与は後日）</span></td></tr>
    <tr><td class="time">16:00～</td><td>懇親会<span class="note">（参加申し込み方のみ）</span></td></tr>
  </table>

  <footer class="footer">
    <div class="org"><span class="dot"></span>森川暮らし連盟</div>
    <p class="apply">申し込みは森川暮らし連盟HPから</p>
    <p class="url">https://www.morikawa-kurashi.example</p>
    <div class="search">
      <span class="box">森川暮らし</span>
      <span class="btn"><svg width="16" height="16" viewBox="0 0 16 16"><circle cx="6.5" cy="6.5" r="4.5" fill="none" stroke="#fff" stroke-width="2"/><line x1="10" y1="10" x2="14.5" y2="14.5" stroke="#fff" stroke-width="2.4"/></svg>検索</span>
    </div>
  </footer>
</div>
</body>
</html>
```